Farm Entrance Sign Design for Estate - Juniper Brook Farm

I am seeking a sign to hang where you turn in my driveway to my farm. The name of the farm is "Juniper Brook Farm". The sign/logo does not need the work "Farm" in it necessarily. The sign should be simple, clean, elegant.

I will attach some basic signs that are of the quality I am seeking. I will also attach a view of the farm entrance. I do not want the sign to compete with the landscape. This is in an area of estate type farms with horses and high end homes.

We are a cattle farm. But don't necessarily have to have cow on sign.

Font styles to use
Sans Serif

Colors

Designer to choose colors to be used in the design.

Requirements
Nice to have
• I prefer a clean font...nothing fancy

```html
<!DOCTYPE html>
<html lang="en">
<head>
<meta charset="utf-8">
<title>Juniper Brook Farm — Entrance Sign</title>
<link rel="stylesheet" href="https://fonts.googleapis.com/css2?family=Cinzel:wght@500&display=swap">
<style>
  :root {
    --backdrop: #d4d4d4;
    --sign-black: #000000;
    --silver-light: #ffffff;
    --silver-mid: #d9d9d9;
    --silver-dark: #9a9a9a;
    --frame-line: #e6e6e6;
    --art-tone-a: #2a2a2a;
    --art-tone-b: #141414;
  }
  * { margin: 0; padding: 0; box-sizing: border-box; }
  html, body {
    width: 1200px;
    height: 1200px;
    overflow: hidden;
    background: var(--backdrop);
  }
  .sign {
    position: absolute;
    left: 124px;
    top: 50px;
    width: 952px;
    height: 1100px;
    background: var(--sign-black);
  }
  .sign-frame {
    position: absolute;
    inset: 0;
    width: 952px;
    height: 1100px;
  }
  .sign-title {
    position: absolute;
    left: 0;
    width: 100%;
    text-align: center;
    font-family: "Cinzel", serif;
    font-weight: 500;
    line-height: 1;
    letter-spacing: 1px;
    background: linear-gradient(180deg, var(--silver-light) 0%, var(--silver-mid) 45%, var(--silver-dark) 100%);
    -webkit-background-clip: text;
    background-clip: text;
    color: transparent;
  }
  .sign-title--the    { top: 78px;  font-size: 116px; }
  .sign-title--first  { top: 192px; font-size: 116px; }
  .sign-title--second { top: 306px; font-size: 116px; }
  .sign-title--farm   { top: 940px; font-size: 116px; }
  .sign-artwork {
    position: absolute;
    left: 261px;
    top: 459px;
    width: 430px;
    height: 436px;
    border-radius: 46% 46% 42% 42%;
    background: radial-gradient(ellipse at 50% 45%, var(--art-tone-a) 0%, var(--art-tone-b) 70%, var(--sign-black) 100%);
  }
</style>
</head>
<body>
  <div class="sign">
    <svg class="sign-frame" viewBox="0 0 952 1100" aria-hidden="true">
      <path d="M75 35 H877 A40 40 0 0 0 917 75 V1025 A40 40 0 0 0 877 1065 H75 A40 40 0 0 0 35 1025 V75 A40 40 0 0 0 75 35 Z"
            fill="none" stroke="var(--frame-line)" stroke-width="2.5"/>
    </svg>
    <div class="sign-title sign-title--the">The</div>
    <div class="sign-title sign-title--first">Juniper</div>
    <div class="sign-title sign-title--second">Brook</div>
    <div class="sign-artwork" role="img" aria-label="White line engraving of fresh berries, two whole and one halved"></div>
    <div class="sign-title sign-title--farm">Farm</div>
  </div>
</body>
</html>
```